CareVantRx business cards

We need a business card design that we could customize as needed for employees. We will need space for Name, Title, 1-2 phone numbers and email address.

We are a Pharmacy Benefits Management (PBM) company for hospice agencies and beginning a nationwide expansion. Attached is a vector file of our logo.

Cards can be single or double sided.

Industry/Entity Type

Business

```html
<!DOCTYPE html>
<html lang="en">
<head>
<meta charset="utf-8">
<title>CareVantRx Business Card</title>
<link rel="stylesheet" href="https://fonts.googleapis.com/css2?family=Ubuntu:wght@300;400;700&family=Ubuntu+Condensed&display=swap">
<style>
  :root {
    --page-bg: #e9ebee;
    --card-white: #ffffff;
    --card-mist: #eef0f2;
    --brand-blue: #3f6f92;
    --brand-green: #8ea35a;
    --text-grey: #4a4f55;
    --rule-grey: #cfd3d7;
    --back-light: #7fa6c2;
    --back-dark: #4c7b9e;
  }
  * { box-sizing: border-box; margin: 0; padding: 0; }
  html, body {
    width: 1200px; height: 1018px; overflow: hidden;
    background: var(--page-bg);
    font-family: "Ubuntu", sans-serif;
  }
  .sheet {
    width: 1200px; height: 1018px;
    display: flex; flex-direction: column; align-items: center;
    justify-content: space-evenly;
  }
  .card {
    width: 780px; height: 446px; position: relative;
    box-shadow: 0 10px 28px rgba(0,0,0,0.18);
    overflow: hidden;
  }
  .card-front {
    background: linear-gradient(120deg, var(--card-white) 35%, var(--card-mist) 100%);
  }
  .side-strip {
    position: absolute; top: 0; right: 0; width: 118px; height: 100%;
    border-left: 1px solid var(--rule-grey);
    background: linear-gradient(180deg, #f6f7f8, var(--card-mist));
  }
  .brand {
    position: absolute; left: 52px; top: 66px;
    display: flex; align-items: center; gap: 16px;
  }
  .brand-mark {
    width: 50px; height: 50px; border-radius: 8px;
    background: var(--brand-blue);
  }
  .brand-name {
    font-size: 58px; font-weight: 400; color: var(--brand-blue);
    letter-spacing: -0.5px; line-height: 1;
  }
  .brand-rule {
    position: absolute; left: 52px; top: 150px; width: 520px; height: 3px;
    background: var(--brand-green);
  }
  .person { position: absolute; left: 52px; top: 184px; }
  .person-name {
    font-family: "Ubuntu Condensed", sans-serif;
    font-size: 30px; letter-spacing: 1px; color: var(--brand-blue);
    text-transform: uppercase;
  }
  .person-title {
    margin-top: 4px; font-size: 13px; letter-spacing: 2px;
    color: var(--text-grey); text-transform: uppercase;
  }
  .contact-rule {
    position: absolute; left: 52px; top: 272px; width: 520px; height: 1px;
    background: var(--rule-grey);
  }
  .contacts {
    position: absolute; left: 52px; top: 292px;
    display: grid; grid-template-columns: 200px 300px; row-gap: 14px;
    font-size: 15px; letter-spacing: 1px; color: var(--text-grey);
  }
  .contact { display: flex; align-items: center; gap: 10px; white-space: nowrap; }
  .contact.wide { grid-column: 1 / span 2; }
  .contact svg { width: 15px; height: 15px; flex: none; }
  .card-back {
    background: linear-gradient(135deg, var(--back-dark) 0%, var(--back-light) 55%, var(--back-dark) 100%);
  }
</style>
</head>
<body>
<main class="sheet">
  <section class="card card-front" aria-label="Card front">
    <div class="side-strip"></div>
    <div class="brand">
      <span class="brand-mark"></span>
      <span class="brand-name">CareVantRx</span>
    </div>
    <div class="brand-rule"></div>
    <div class="person">
      <p class="person-name">Dana Whitfield</p>
      <p class="person-title">General Manager</p>
    </div>
    <div class="contact-rule"></div>
    <div class="contacts">
      <span class="contact">
        <svg viewBox="0 0 16 16" fill="var(--brand-blue)"><path d="M3.5 1.5l2.5 0 1 3.5-1.6 1.2a9 9 0 0 0 4.4 4.4L11 9l3.5 1v2.5c0 1-1 2-2 2C6.5 14.5 1.5 9.5 1.5 3.5c0-1 1-2 2-2z"/></svg>
        014 628 3370
      </span>
      <span class="contact">
        <svg viewBox="0 0 16 16" fill="var(--brand-blue)"><rect x="1" y="3" width="14" height="10" rx="1"/><path d="M1.5 4l6.5 5 6.5-5" stroke="#fff" stroke-width="1.3" fill="none"/></svg>
        dana@carevantrx.com
      </span>
      <span class="contact">
        <svg viewBox="0 0 16 16" fill="none" stroke="var(--brand-blue)" stroke-width="1.6"><rect x="4" y="1.5" width="8" height="13" rx="1.5"/><circle cx="8" cy="12" r="0.8" fill="var(--brand-blue)"/></svg>
        014 628 3371
      </span>
      <span class="contact">
        <svg viewBox="0 0 16 16" fill="none" stroke="var(--brand-blue)" stroke-width="1.4"><circle cx="8" cy="8" r="6.5"/><ellipse cx="8" cy="8" rx="3" ry="6.5"/><path d="M1.5 8h13"/></svg>
        www.carevantrx.com
      </span>
      <span class="contact wide">
        <svg viewBox="0 0 16 16" fill="var(--brand-blue)"><path d="M8 1a5 5 0 0 1 5 5c0 3.5-5 9-5 9S3 9.5 3 6a5 5 0 0 1 5-5z"/><circle cx="8" cy="6" r="1.8" fill="#fff"/></svg>
        212 Harbor Ridge Road, Suite 3, Westfield
      </span>
    </div>
  </section>
  <section class="card card-back" aria-label="Card back"></section>
</main>
</body>
</html>
```